Business Card Design

I'm a Naturopathic Physician specializing in the treatment of autoimmune disorders, supportive cancer care and stress, anxiety and depressive disorders.

I practice out of 3 clinic locations and I want a business card design which can be easily changed to include 3 clinic locations, addresses, and contact info.

My website is VeltarisHealth.com and this will promote me personally as a specialist in these treatment areas. I would like one side of the business card to promote this site with the tag line "Specializing in Immune and Related Disorders"

REVIEW THE DESCRIPTION AND UPLOADS FOR MY DESIGN STYLE PREFERENCES.

Industry/Entity Type

Clinic

Colors
9bcb3c
fbed22
0455a3

Requirements
Must have
• Would prefer a vertical design.
Would like bold, simple colors and contrasts

Please visit http://plovexa.com/veltarishealth/ for some color and design "feel"

Do not feel the Designs HAVE to have the logo in it... I want SIMPLE, CLEAN and BOLD design so if the Logo makes the designs too busy, please omit

Dr. Marcus Fenholt BSc ND
Naturopathic Physician

"Clinic Name"
"Clinic Address"
"Clinic Tel"
"Clinic E-Mail"
"Clinic Website"

Please review the PDF for design styles I prefer.

Please Note: Once I determine if there are design concepts worthy of going forward with, I will forward specific contact and clinic information at that time for final design

```html
<!DOCTYPE html>
<html lang="en">
<head>
<meta charset="utf-8">
<title>VeltarisHealth Business Card</title>
<link rel="stylesheet" href="https://fonts.googleapis.com/css2?family=Jost:wght@600;700&display=swap">
<style>
  :root {
    --page-bg: #ffffff;
    --band-green: #8dc21f;
    --band-green-dark: #6f9e12;
    --field-blue: #0a9bef;
    --field-blue-light: #8fd4ff;
    --field-blue-deep: #0a7fd0;
    --emblem-green: #7cb51c;
    --emblem-ring: #c9ccce;
    --text-white: #ffffff;
  }
  * { margin: 0; padding: 0; box-sizing: border-box; }
  html, body {
    width: 1200px;
    height: 1000px;
    overflow: hidden;
    background: var(--page-bg);
  }
  .canvas {
    position: relative;
    width: 1200px;
    height: 1000px;
  }
  .business-card {
    position: absolute;
    left: 100px;
    top: 215px;
    width: 1000px;
    height: 570px;
    overflow: hidden;
    background: radial-gradient(circle at 30% 50%, var(--field-blue-light) 0%, var(--field-blue) 30%, var(--field-blue-deep) 100%);
    box-shadow: 0 6px 18px rgba(0, 0, 0, 0.18);
    font-family: "Jost", "Century Gothic", sans-serif;
  }
  .tagline-band,
  .website-band {
    position: absolute;
    left: 0;
    width: 100%;
    background: linear-gradient(to bottom, var(--band-green) 0%, var(--band-green) 85%, var(--band-green-dark) 100%);
    display: flex;
    align-items: center;
    justify-content: center;
    color: var(--text-white);
    z-index: 2;
  }
  .tagline-band {
    top: 14px;
    height: 84px;
  }
  .tagline {
    font-weight: 600;
    font-size: 43px;
    letter-spacing: 0.2px;
    text-shadow: 0 2px 3px rgba(0, 0, 0, 0.2);
  }
  .website-band {
    bottom: 12px;
    height: 98px;
  }
  .website {
    font-weight: 700;
    font-size: 64px;
    text-shadow: 0 2px 4px rgba(0, 0, 0, 0.25);
  }
  .decor-ring {
    position: absolute;
    right: -330px;
    top: -60px;
    width: 760px;
    height: 760px;
    z-index: 3;
    pointer-events: none;
  }
  .brand-mark {
    position: absolute;
    left: 160px;
    top: 200px;
    display: flex;
    align-items: center;
    gap: 22px;
    z-index: 2;
  }
  .brand-circle {
    width: 190px;
    height: 190px;
    border-radius: 50%;
    background: var(--emblem-green);
    border: 14px solid var(--emblem-ring);
    box-shadow: 0 4px 10px rgba(0, 0, 0, 0.3);
  }
  .brand-name {
    font-weight: 700;
    font-size: 46px;
    color: var(--text-white);
  }
</style>
</head>
<body>
<main class="canvas">
  <section class="business-card" aria-label="Business card front">
    <header class="tagline-band">
      <p class="tagline">Specializing in Immune and Related Disorders</p>
    </header>

    <div class="brand-mark">
      <span class="brand-circle" aria-hidden="true"></span>
      <span class="brand-name">VeltarisHealth</span>
    </div>

    <svg class="decor-ring" viewBox="0 0 760 760" aria-hidden="true">
      <circle cx="380" cy="380" r="350" fill="rgba(255,255,255,0.10)" stroke="rgba(255,255,255,0.22)" stroke-width="30"/>
    </svg>

    <footer class="website-band">
      <p class="website">www.VeltarisHealth.com</p>
    </footer>
  </section>
</main>
</body>
</html>
```